T Varlo

Ned a new business card, need two designs one to be for communications and one to be for security.
Communications will have what we do on it which include:-
PABX systems
Data Cabling
Phone services
Fibre
Security
"your communications specialist in the Pilbara"
The Severity one will have on it:-
CCTV
Alarm
Access control
Security consulting
Communications services
"Your security partner in the Pilbara"
Target Market(s)
industry
Industry/Entity Type
Communications
Contact Information for Business Card
Marcus Delby
0493726051
marcus@tvarlo.com.au
www.tvarlo.com.au

```html
<!DOCTYPE html>
<html lang="en">
<head>
<meta charset="utf-8">
<title>T Varlo — Business Cards</title>
<link rel="stylesheet" href="https://fonts.googleapis.com/css2?family=Open+Sans:wght@400;600&display=swap">
<style>
  :root {
    --backdrop: #0a94a8;
    --divider: #ffffff;
    --card: #f4f4f2;
    --ink-grey: #5f5f61;
    --band-grey: #636365;
    --accent: #e2a03a;
    --paper-text: #ffffff;
  }
  * { box-sizing: border-box; margin: 0; padding: 0; }
  html, body { width: 1200px; height: 1000px; overflow: hidden; }
  body {
    background: var(--backdrop);
    font-family: "Open Sans", Arial, sans-serif;
    position: relative;
  }
  .set { position: absolute; left: 0; width: 1200px; height: 498px; }
  .set--communications { top: 0; }
  .set--security { top: 502px; }
  .divider { position: absolute; left: 0; top: 498px; width: 1200px; height: 4px; background: var(--divider); }

  .card {
    position: absolute;
    width: 500px; height: 286px;
    background: var(--card);
    box-shadow: 0 10px 24px rgba(0,0,0,0.18);
  }
  .card--front { left: 70px; top: 40px; }
  .card--back { left: 630px; top: 175px; }

  .brand {
    position: absolute; left: 0; top: 0; width: 100%; height: 100%;
    display: flex; align-items: center; justify-content: center; gap: 14px;
  }
  .brand__dot { width: 22px; height: 22px; border-radius: 50%; background: var(--accent); }
  .brand__name { font-size: 54px; font-weight: 600; color: var(--accent); letter-spacing: 1px; }

  .details { position: absolute; left: 0; top: 0; width: 100%; height: 100%; }
  .details__name {
    position: absolute; left: 30px; top: 72px;
    font-size: 25px; color: var(--ink-grey); font-weight: 400;
  }
  .band { position: absolute; left: 22px; color: var(--paper-text); white-space: nowrap; }
  .band--tagline {
    top: 108px; height: 30px; width: 370px; background: var(--band-grey);
    font-size: 17px; line-height: 30px; padding-left: 10px; font-style: italic;
  }
  .band--services {
    top: 138px; width: 478px; background: var(--accent);
    font-size: 13px; line-height: 18px; padding: 6px 10px; text-transform: uppercase; white-space: normal;
    word-spacing: 2px;
  }
  .band--services span { margin-right: 10px; }
  .contacts { position: absolute; left: 32px; list-style: none; font-size: 17px; color: var(--ink-grey); line-height: 25px; }
  .contacts--communications { top: 178px; }
  .contacts--security { top: 190px; }
  .contacts__label { color: var(--accent); margin-right: 4px; }
</style>
</head>
<body>
  <section class="set set--communications" aria-label="Communications card">
    <div class="card card--front">
      <div class="brand">
        <span class="brand__dot"></span>
        <span class="brand__name">T Varlo</span>
      </div>
    </div>
    <div class="card card--back">
      <div class="details">
        <p class="details__name">Marcus Delby</p>
        <p class="band band--tagline">your communications specialist in the Pilbara</p>
        <p class="band band--services">
          <span>PABX Systems</span><span>Data Cabling</span><span>Phone Services</span><span>Fibre</span><span>Security</span>
        </p>
        <ul class="contacts contacts--communications">
          <li><span class="contacts__label">t::</span>0493726051</li>
          <li><span class="contacts__label">e::</span>marcus@tvarlo.com.au</li>
          <li><span class="contacts__label">w::</span>www.tvarlo.com.au</li>
        </ul>
      </div>
    </div>
  </section>

  <div class="divider"></div>

  <section class="set set--security" aria-label="Security card">
    <div class="card card--front">
      <div class="brand">
        <span class="brand__dot"></span>
        <span class="brand__name">T Varlo</span>
      </div>
    </div>
    <div class="card card--back">
      <div class="details">
        <p class="details__name">Marcus Delby</p>
        <p class="band band--tagline">your security partner in the Pilbara</p>
        <p class="band band--services">
          <span>Alarm</span><span>Access Control</span><span>Security Consulting</span><br>
          <span>Communications Services</span><span>CCTV</span>
        </p>
        <ul class="contacts contacts--security">
          <li><span class="contacts__label">t::</span>0493726051</li>
          <li><span class="contacts__label">e::</span>marcus@tvarlo.com.au</li>
          <li><span class="contacts__label">w::</span>www.tvarlo.com.au</li>
        </ul>
      </div>
    </div>
  </section>
</body>
</html>
```